WordPress design needed for scientist

Hi! I am a female scientist (36 years old) in the field of marine science and biotechnology. I need a clean, engaging, modern WordPress website design. Not just a blog, but a site that shows pictures of my research and topics, can host PDFs of my research publications, and can have my Chirplinefeed (@miraveltrosk) and Vidoplex videos embedded. Something a bit like this: http://www.pelmarine.org.uk/ but with my content, and a more engaging design, like the template "FJORD"

My current webprofile from the University of Norlund is here: http://www.uon.no/personer/Mira.Ellen.Veltrosk , but I need something that is more than this, that can inspire grant evaluators to pick me, and a website that shows the best sides of me and my research. I attach some representative pictures of me and my research that I would like to be used/incorporated in the webdesign.

Target Market(s)

other scientists, journalists, media, interested members of the public

Industry/Entity Type

Biotechnology

Font styles to use
Sans Serif

Requirements
Must have
• Vidoplex video embedding of these videos:
• https://www.vidoplex.com/watch?v=7QkTRBmwZa2
• https://www.vidoplex.com/watch?v=Hp3dLxeVnR8
• https://www.vidoplex.com/watch?v=Zu9KcWtbEq4
• Slidora Presentations embedded: https://slidora.com/user/miraveltrosk/

```html
<!DOCTYPE html>
<html lang="en">
<head>
<meta charset="utf-8">
<title>Mira E. Veltrosk PhD</title>
<link href="https://fonts.googleapis.com/css2?family=Libre+Baskerville:wght@400;700&family=Open+Sans:wght@400;600;700&display=swap" rel="stylesheet">
<style>
:root{
  --ink:#1c1c1c;
  --muted:#6b6b6b;
  --accent:#8a5a3c;
  --panel:#ffffff;
  --card:#f7f6f4;
  --border:#d9d9d9;
  --footer:#050505;
  --ocean-top:#4a3a2a;
  --ocean-mid:#1c3346;
  --ocean-deep:#0d1b2c;
}
*{box-sizing:border-box;margin:0;padding:0}
html,body{width:941px;height:1200px;overflow:hidden}
body{
  position:relative;
  font-family:"Open Sans",sans-serif;
  color:var(--ink);
  background:linear-gradient(180deg,var(--ocean-top) 0%,#3b4a52 10%,var(--ocean-mid) 35%,var(--ocean-deep) 80%,#0a1624 100%);
}
.site-title{
  position:absolute;left:76px;top:48px;
  font-family:"Libre Baskerville",serif;font-weight:700;font-size:17px;color:#fff;letter-spacing:.3px;
}
.main-nav{position:absolute;top:50px;left:346px;height:44px;display:flex;gap:3px}
.main-nav a{
  display:flex;align-items:center;justify-content:center;height:44px;
  background:var(--panel);border-top:3px solid #d8c9b0;border-radius:4px 4px 0 0;
  font-family:"Libre Baskerville",serif;font-size:11.5px;color:var(--ink);text-decoration:none;
}
.panel{position:absolute;left:77px;top:94px;width:786px;height:987px;background:var(--panel)}
.hero{
  position:absolute;left:9px;top:11px;width:768px;height:307px;border-radius:4px;
  background:linear-gradient(90deg,#e9e3c6 0%,#ddd3b0 45%,#b69a7a 75%,#5b4536 100%);
  overflow:hidden;
}
.hero-text{position:absolute;left:30px;top:122px}
.hero-kicker{font-family:"Libre Baskerville",serif;font-size:18px;color:#222}
.hero-title{font-family:"Libre Baskerville",serif;font-weight:700;font-size:31px;color:#111;margin-top:6px}
.dots{position:absolute;left:31px;top:323px;display:flex;gap:4px}
.panel .dots{top:319px;left:40px}
.dots span{width:13px;height:13px;border-radius:50%;border:1.5px solid #fff;display:block}
.dots span.on{background:var(--accent)}
.section-head{
  position:absolute;left:9px;width:768px;display:flex;align-items:center;gap:12px;
  font-family:"Libre Baskerville",serif;font-weight:700;font-size:17px;white-space:nowrap;
}
.section-head::before,.section-head::after{content:"";flex:1;height:4px;border-top:1px solid var(--border);border-bottom:1px solid var(--border)}
.card-row{position:absolute;left:9px;width:768px;display:flex;gap:15px}
.video-card{width:246px;height:163px;border:1px solid var(--border);border-radius:4px;padding:3px;background:#fff}
.video-frame{position:relative;width:100%;height:100%}
.video-bar{
  position:absolute;left:0;right:0;top:0;height:32px;padding:0 8px;display:flex;align-items:center;justify-content:space-between;
  background:linear-gradient(180deg,rgba(0,0,0,.45),rgba(0,0,0,0));
  color:#fff;font-weight:700;font-size:11px;letter-spacing:.2px;
}
.video-bar svg{margin-left:6px}
.play{position:absolute;left:50%;top:50%;width:36px;height:36px;margin:-18px 0 0 -18px}
.pres-card{width:246px;height:306px;border:1px solid var(--border);border-radius:4px;padding:3px;background:var(--card);text-align:center}
.pres-photo{height:146px;border-radius:2px}
.pres-title{font-family:"Libre Baskerville",serif;font-weight:700;font-size:13px;margin-top:17px}
.pres-body{font-size:10px;line-height:18.5px;color:var(--muted);margin:10px 10px 0}
.read-more{display:block;margin-top:9px;font-size:10.5px;font-weight:700;color:var(--accent);text-decoration:none}
.site-footer{position:absolute;left:77px;top:1081px;width:786px;height:70px;background:var(--footer);color:#fff;font-size:10px}
.footer-links{position:absolute;left:10px;top:19px}
.footer-links span{margin:0 5px}
.copyright{position:absolute;left:10px;top:39px}
.social{position:absolute;right:9px;top:19px;display:flex;gap:5px}
.social a{width:32px;height:32px;border:1.5px solid #fff;border-radius:50%;display:flex;align-items:center;justify-content:center;color:#fff;text-decoration:none;font-size:7px;font-weight:600}
</style>
</head>
<body>
<div class="site-title">MIRA E. VELTROSK PHD</div>
<nav class="main-nav">
  <a href="#" style="width:125px">PUBLICATIONS</a>
  <a href="#" style="width:96px">BIO</a>
  <a href="#" style="width:95px">PROJECTS</a>
  <a href="#" style="width:96px">VISION</a>
  <a href="#" style="width:95px">CONTACT</a>
</nav>

<main class="panel">
  <section class="hero" role="img" aria-label="Portrait of the scientist smiling, soft beige background">
    <div class="hero-text">
      <div class="hero-kicker">Making connections in</div>
      <div class="hero-title">Marine Science &amp; Society</div>
    </div>
  </section>
  <div class="dots"><span class="on"></span><span></span><span></span></div>

  <h2 class="section-head" style="top:354px">LATEST VIDEOS</h2>
  <div class="card-row" style="top:397px">
    <div class="video-card"><div class="video-frame" role="img" aria-label="Video still of the scientist presenting in a classroom" style="background:linear-gradient(90deg,#5d7a43,#8a8f8c 30%,#3f8b7a 60%,#9aa3a5)">
      <div class="video-bar"><span>"HOW TO SAVE THE ...</span><span><svg width="16" height="16" viewBox="0 0 16 16"><circle cx="8" cy="8" r="6.5" fill="none" stroke="#fff" stroke-width="1.6"/><path d="M8 4.5V8h2.5" fill="none" stroke="#fff" stroke-width="1.6"/></svg><svg width="20" height="16" viewBox="0 0 20 16"><path d="M2 14c1-6 5-8 11-8V2l6 6-6 6V10c-5 0-8 1-11 4z" fill="#fff"/></svg></span></div>
      <svg class="play" viewBox="0 0 36 36"><circle cx="18" cy="18" r="18" fill="rgba(20,20,20,.8)"/><path d="M14 11l11 7-11 7z" fill="#fff"/></svg>
    </div></div>
    <div class="video-card"><div class="video-frame" role="img" aria-label="Video still of the scientist speaking on a conference stage" style="background:linear-gradient(180deg,#4f86e0 0%,#7aa6ea 55%,#1a1a1a 72%,#6b1a14 100%)">
      <div class="video-bar"><span>" FISHERIES MANAGEMENT...</span><span><svg width="16" height="16" viewBox="0 0 16 16"><circle cx="8" cy="8" r="6.5" fill="none" stroke="#fff" stroke-width="1.6"/><path d="M8 4.5V8h2.5" fill="none" stroke="#fff" stroke-width="1.6"/></svg><svg width="20" height="16" viewBox="0 0 20 16"><path d="M2 14c1-6 5-8 11-8V2l6 6-6 6V10c-5 0-8 1-11 4z" fill="#fff"/></svg></span></div>
      <svg class="play" viewBox="0 0 36 36"><circle cx="18" cy="18" r="18" fill="rgba(20,20,20,.8)"/><path d="M14 11l11 7-11 7z" fill="#fff"/></svg>
    </div></div>
    <div class="video-card"><div class="video-frame" role="img" aria-label="Video still of a diver over a coral reef" style="background:linear-gradient(180deg,#3a8a8a 0%,#2f7070 55%,#5a6a5c 100%)">
      <div class="video-bar"><span>MIRA VELTROSK TIDEWIRE...</span><span><svg width="16" height="16" viewBox="0 0 16 16"><circle cx="8" cy="8" r="6.5" fill="none" stroke="#fff" stroke-width="1.6"/><path d="M8 4.5V8h2.5" fill="none" stroke="#fff" stroke-width="1.6"/></svg><svg width="20" height="16" viewBox="0 0 20 16"><path d="M2 14c1-6 5-8 11-8V2l6 6-6 6V10c-5 0-8 1-11 4z" fill="#fff"/></svg></span></div>
      <svg class="play" viewBox="0 0 36 36"><circle cx="18" cy="18" r="18" fill="rgba(20,20,20,.8)"/><path d="M14 11l11 7-11 7z" fill="#fff"/></svg>
    </div></div>
  </div>

  <h2 class="section-head" style="top:593px">LATEST PRESENTATIONS</h2>
  <div class="card-row" style="top:639px">
    <article class="pres-card">
      <div class="pres-photo" role="img" aria-label="Workshop participants around a meeting table" style="background:linear-gradient(180deg,#8d8f93,#a89a86 55%,#d4c7b0)"></div>
      <h3 class="pres-title">Finibus Bonorum Maloruet</h3>
      <p class="pres-body">At vero eos et accusamus et iusto odiomos ducimus qui blanditiis praesentium voluptalique sunt in culpa qui officia deserunt rerum facilis est et expediesentta distinctio.</p>
      <a class="read-more" href="#">READ MORE &gt;&gt;</a>
    </article>
    <article class="pres-card">
      <div class="pres-photo" role="img" aria-label="Researchers working on laptops at a seminar table" style="background:linear-gradient(180deg,#6e5a4a,#8f7c6c 45%,#3a3634)"></div>
      <h3 class="pres-title">Finibus Bonorum Maloruet</h3>
      <p class="pres-body">At vero eos et accusamus et iusto odiomos ducimus qui blanditiis praesentium voluptalique sunt in culpa qui officia deserunt rerum facilis est et expediesentta distinctio.</p>
      <a class="read-more" href="#">READ MORE &gt;&gt;</a>
    </article>
    <article class="pres-card">
      <div class="pres-photo" role="img" aria-label="Seminar room with a projected presentation" style="background:linear-gradient(180deg,#5a4a3e,#7a6a58 50%,#2e2a28)"></div>
      <h3 class="pres-title">Finibus Bonorum Maloruet</h3>
      <p class="pres-body">At vero eos et accusamus et iusto odiomos ducimus qui blanditiis praesentium voluptalique sunt in culpa qui officia deserunt rerum facilis est et expediesentta distinctio.</p>
      <a class="read-more" href="#">READ MORE &gt;&gt;</a>
    </article>
  </div>
</main>

<footer class="site-footer">
  <div class="footer-links">Publications<span>|</span>Bio<span>|</span>Projects<span>|</span>Vision<span>|</span>Contact Us</div>
  <div class="copyright">Copyright © 2016, Mira E. Veltrosk. All rights Reserved.</div>
  <div class="social"><a href="#">Folio</a><a href="#">Chirp</a><a href="#">Orbit</a></div>
</footer>
</body>
</html>
```